Salon website

Need a web design for a new blow dry and hair extension boutique in CT
would like the color scheme to be gray, white and tiffany blue
Create a web site with about 4 pages showing
1 about us page
1 blow dry services page
1 hair extension services page
1 contact us page
1 membership page
1 parties page

Industry/Entity Type

Boutique

Colors
86cfc6
cfeae6
33b7a4
aaaaaa
cbcbcb
ffffff

```html
<!DOCTYPE html>
<html lang="en">
<head>
<meta charset="utf-8">
<title>Contact Us – Salon Name</title>
<link href="https://fonts.googleapis.com/css2?family=Questrial&family=Lato:wght@400&display=swap" rel="stylesheet">
<style>
  :root {
    --tiffany: #82d8cf;
    --gray: #cccccc;
    --white: #ffffff;
    --photo-dark: #2a2a2a;
    --photo-light: #8a8a8a;
  }
  * { margin: 0; padding: 0; box-sizing: border-box; }
  html, body {
    width: 1200px;
    height: 1000px;
    overflow: hidden;
    background: var(--white);
    color: var(--white);
    font-family: "Questrial", "Century Gothic", sans-serif;
  }
  .page { position: relative; width: 1200px; height: 1000px; }

  .logo-block {
    position: absolute; left: 0; top: 0;
    width: 223px; height: 145px;
    background: var(--tiffany);
  }
  .main-nav {
    position: absolute; left: 243px; top: 0;
    width: 957px; height: 145px;
    background: var(--tiffany);
  }
  .main-nav a {
    position: absolute; top: 55px;
    font-size: 25px; line-height: 32px;
    color: var(--white); text-decoration: none;
    white-space: nowrap;
  }
  .nav-about { left: 37px; }
  .nav-blowdry { left: 240px; }
  .nav-extensions { left: 462px; }
  .nav-contact { left: 764px; }

  .contact-section {
    position: absolute; left: 0; top: 194px;
    width: 1200px; height: 590px;
    background: var(--gray);
  }
  .contact-title {
    position: absolute; left: 26px; top: 26px;
    font-size: 34px; font-weight: 400; line-height: 44px;
    white-space: nowrap;
  }
  .contact-details {
    position: absolute; left: 93px; top: 98px;
    width: 760px;
    font-family: "Lato", "Gill Sans", sans-serif;
    font-size: 23px; line-height: 30px;
  }
  .contact-details p { white-space: pre; }
  .gap-sm { margin-top: 30px; }
  .gap-lg { margin-top: 60px; }
  .directions { list-style: none; }
  .directions li { white-space: pre; }

  .storefront-frame {
    position: absolute; left: 890px; top: 56px;
    width: 302px; height: 498px;
    background: var(--white);
    padding: 10px 8px 8px 10px;
  }
  .storefront-photo {
    width: 284px; height: 480px;
    background: linear-gradient(180deg, var(--photo-dark) 0%, var(--photo-light) 55%, var(--photo-dark) 100%);
  }

  .site-footer {
    position: absolute; left: 0; top: 843px;
    width: 1200px; height: 157px;
    background: var(--tiffany);
  }
  .site-footer span, .site-footer a {
    position: absolute; top: 88px;
    font-size: 26px; line-height: 32px;
    color: var(--white); text-decoration: none;
    white-space: nowrap;
  }
  .footer-copy { left: 333px; }
  .footer-privacy { left: 656px; }
</style>
</head>
<body>
<div class="page">
  <div class="logo-block"></div>
  <nav class="main-nav">
    <a class="nav-about" href="#">ABOUT US</a>
    <a class="nav-blowdry" href="#">BLOW DRY</a>
    <a class="nav-extensions" href="#">HAIR EXTENSIONS</a>
    <a class="nav-contact" href="#">CONTACT US</a>
  </nav>

  <section class="contact-section">
    <h1 class="contact-title">CONTACT US</h1>
    <div class="contact-details">
      <p>P   555.014.2280</p>
      <p>F   555.014.2281</p>
      <p class="gap-sm">E   HELLO@BLOWBAR.EXAMPLE</p>
      <p class="gap-sm">48 ELM HARBOR ROAD</p>
      <p>BAYVIEW, CT 06999</p>
      <p class="gap-lg">DIRECTIONS:</p>
      <ol class="directions">
        <li>1  Vivamus eu nunc vel velit fringilla convallis vel et lacus.</li>
        <li>2  Nam vel elit blandit, rhoncus leo et, ultricies turpis.</li>
        <li>3  Ut pharetra quam ipsum, quis placerat lectus rhoncus a.</li>
      </ol>
    </div>
    <div class="storefront-frame">
      <div class="storefront-photo" role="img" aria-label="Black and white photo of the salon storefront with tall glass doors and windows"></div>
    </div>
  </section>

  <footer class="site-footer">
    <span class="footer-copy">© 2014 SALON NAME</span>
    <a class="footer-privacy" href="#">PRIVACY POLICY</a>
  </footer>
</div>
</body>
</html>
```